Lumora aesthetics offers a range of facial aesthetics treatments by a fully qualified dentist, to a high end crowd. Treatments include antiwrinkle treatment, the use of dermal fillers to provide facial volumisation and rejuvenation and also lip volumisation.
I want a luxurious and bold look. Black background with a bold striking gold logo in the centre possibly incorporating the outline of a face in a subtle yet effective way. I want it to include the work I offer so people will be aware of what they are looking into but not look like there's too much on the card, So it's a clean look.
At the bottom I would like it to say by Dr. Meera Sandhu. Alongside my email address and mobile number.

```html
<!DOCTYPE html>
<html lang="en">
<head>
<meta charset="utf-8">
<title>Lumora Aesthetics – Business Card</title>
<link rel="stylesheet" href="https://fonts.googleapis.com/css2?family=Cinzel:wght@400;500&family=Josefin+Sans:wght@700&display=swap">
<style>
  :root {
    --stage: #d6d6d6;
    --card-black: #0a0a0a;
    --gold-bright: #f7d54a;
    --gold-light: #f6e08e;
    --gold-deep: #c9a23a;
    --bronze: #6b3f12;
    --bronze-dark: #3a2008;
    --muted-gold: #b8933a;
  }
  * { margin: 0; padding: 0; box-sizing: border-box; }
  html, body {
    width: 1200px; height: 841px; overflow: hidden;
    background: var(--stage);
  }
  .business-card {
    position: absolute; left: 100px; top: 134px;
    width: 1000px; height: 572px;
    background: var(--card-black);
    overflow: hidden;
  }
  .card-swoosh { position: absolute; inset: 0; width: 100%; height: 100%; }
  .brand-mark {
    position: absolute; left: 470px; top: 48px;
    width: 86px; height: 86px;
    border: 2px solid var(--gold-bright); border-radius: 50%;
  }
  .brand-name {
    position: absolute; left: 455px; top: 148px;
    font-family: "Cinzel", serif; font-weight: 400;
    color: var(--gold-bright);
    font-size: 52px; line-height: 1; letter-spacing: 1px;
    text-transform: uppercase;
  }
  .brand-name .line-two { display: block; }
  .practitioner {
    position: absolute; left: 50px; top: 208px;
    width: 390px;
  }
  .practitioner-name {
    font-family: "Josefin Sans", sans-serif; font-weight: 700;
    color: var(--gold-bright); font-size: 34px; letter-spacing: 1px;
    text-transform: uppercase; white-space: nowrap;
  }
  .contact-line {
    font-family: "Cinzel", serif; color: var(--muted-gold);
    font-size: 14px; letter-spacing: 1px; margin-top: 8px;
  }
  .contact-line.phone { margin-left: 36px; margin-top: 2px; }
  .divider {
    position: absolute; left: 470px; top: 272px;
    width: 2px; height: 108px; background: var(--gold-bright);
  }
  .treatments {
    position: absolute; left: 490px; top: 276px;
    font-family: "Cinzel", serif; color: var(--gold-bright);
  }
  .treatments-title { font-size: 24px; letter-spacing: 3px; font-weight: 500; }
  .treatment-columns { display: flex; gap: 30px; margin-top: 8px; }
  .treatment-list { list-style: none; font-size: 11px; line-height: 1.15; letter-spacing: 0.5px; width: 200px; }
  .treatment-list li { margin-bottom: 6px; }
</style>
</head>
<body>
  <section class="business-card">
    <svg class="card-swoosh" viewBox="0 0 1000 572" preserveAspectRatio="none" aria-hidden="true">
      <defs>
        <linearGradient id="goldSweep" x1="0" y1="0" x2="1" y2="0.4">
          <stop offset="0" stop-color="#c9a23a"/>
          <stop offset="0.5" stop-color="#f7d54a"/>
          <stop offset="1" stop-color="#f6e08e"/>
        </linearGradient>
        <linearGradient id="bronzeSweep" x1="0" y1="0" x2="1" y2="0">
          <stop offset="0" stop-color="#6b3f12"/>
          <stop offset="1" stop-color="#3a2008"/>
        </linearGradient>
      </defs>
      <path class="bronze-band" d="M0,300 C180,340 380,420 560,530 L480,572 L0,572 Z" fill="url(#bronzeSweep)"/>
      <path class="black-under" d="M0,380 C200,430 420,500 600,572 L0,572 Z" fill="#0a0a0a"/>
      <path class="gold-band" d="M0,335 C260,405 560,480 1000,440 L1000,572 L640,572 C460,490 220,410 0,360 Z" fill="url(#goldSweep)"/>
      <path class="gold-rule" d="M0,335 C260,405 560,480 1000,440" fill="none" stroke="#f7d54a" stroke-width="3"/>
    </svg>

    <div class="brand-mark" aria-hidden="true"></div>
    <h1 class="brand-name">Lumora<span class="line-two">Aesthetics</span></h1>

    <div class="practitioner">
      <p class="practitioner-name">Dr. Meera Sandhu</p>
      <p class="contact-line email">DRMEERASANDHU@LUMORAMAIL.COM</p>
      <p class="contact-line phone">+0000 000 000</p>
    </div>

    <div class="divider"></div>

    <div class="treatments">
      <h2 class="treatments-title">TREATMENTS INCLUDE:</h2>
      <div class="treatment-columns">
        <ul class="treatment-list">
          <li>ANTIWRINKLE<br>TREATMENT</li>
          <li>TREATMENT FOR<br>CLENCHING AND GRINDING</li>
          <li>CHEEK VOLUMISATION</li>
        </ul>
        <ul class="treatment-list">
          <li>TREATMENT FOR EXCESS<br>SWEATING</li>
          <li>REDUCTION OF<br>NASOLABIAL FOLDS</li>
          <li>REDUCTION IN JAW SIZE</li>
        </ul>
      </div>
    </div>
  </section>
</body>
</html>
```